HarmoNest Ensemble Jubilee
Date: Sunday Oct 2, 2022
When: 2-4 p.m.
Location: Brindle9 Alehouse
413 Marlowe Ct #200, Sacramento, CA 95821
Tickets: www.Tixolvo.com
General seating: $15 for adults and $10 for students

```html
<!DOCTYPE html>
<html lang="en">
<head>
<meta charset="utf-8">
<title>HarmoNest Ensemble Jubilee</title>
<link rel="stylesheet" href="https://fonts.googleapis.com/css2?family=Bebas+Neue&family=Yellowtail&family=Yeseva+One&display=swap">
<style>
  :root {
    --gold: #d9a425;
    --gold-light: #f3d257;
    --gold-dark: #a87a12;
    --cream: #f7ecd2;
    --cream-light: #fdf8ea;
    --silver: #b9b9bd;
    --ink: #222222;
    --ink-soft: #3a3a3a;
    --red: #a30006;
    --photo-grey: #d4d4da;
    --white: #ffffff;
  }
  * { box-sizing: border-box; margin: 0; padding: 0; }
  html, body { width: 990px; height: 1200px; overflow: hidden; background: #888; }
  .poster {
    position: relative;
    width: 990px;
    height: 1200px;
    background: linear-gradient(160deg, var(--gold-light), var(--gold) 45%, var(--gold-dark));
    padding: 28px;
  }
  .poster-inner {
    position: relative;
    width: 100%;
    height: 100%;
    border: 4px solid var(--silver);
    background:
      radial-gradient(circle at 12% 8%, rgba(255,255,255,.7) 0 40px, transparent 42px),
      radial-gradient(circle at 85% 6%, rgba(255,255,255,.6) 0 30px, transparent 32px),
      radial-gradient(circle at 92% 78%, rgba(255,255,255,.5) 0 36px, transparent 38px),
      radial-gradient(circle at 6% 82%, rgba(255,255,255,.45) 0 44px, transparent 46px),
      radial-gradient(ellipse at 50% 20%, var(--cream-light), var(--cream) 70%);
    overflow: hidden;
  }
  .title-script {
    position: absolute;
    top: 78px; left: 0; right: 0;
    text-align: center;
    font-family: "Yellowtail", cursive;
    font-size: 84px;
    line-height: 1;
    color: var(--ink);
    background: linear-gradient(180deg, #111 0 55%, #777 70%, #222 100%);
    -webkit-background-clip: text;
    background-clip: text;
    -webkit-text-fill-color: transparent;
  }
  .rule {
    position: absolute;
    left: 97px; right: 97px;
    height: 2px;
    background: var(--ink);
  }
  .rule-top { top: 165px; }
  .rule-bottom { top: 273px; }
  .title-caps {
    position: absolute;
    top: 178px; left: 0; right: 0;
    text-align: center;
    font-family: "Bebas Neue", sans-serif;
    font-size: 92px;
    line-height: 1;
    letter-spacing: 26px;
    padding-left: 26px;
    color: var(--gold);
    text-shadow: 3px 3px 0 var(--ink);
  }
  .photo {
    position: absolute;
    left: 0; top: 250px;
    width: 930px; height: 560px;
  }
  .date-bar {
    position: absolute;
    top: 785px; left: 133px;
    width: 666px; height: 84px;
    border: 4px solid var(--gold);
    display: flex;
    background: linear-gradient(90deg, #111, #2b2b2b);
    overflow: hidden;
  }
  .date-bar .date {
    position: relative;
    width: 438px;
    background: var(--red);
    clip-path: polygon(0 0, 100% 0, 92% 100%, 0 100%);
    font-family: "Bebas Neue", sans-serif;
    font-size: 60px;
    line-height: 78px;
    color: var(--white);
    padding-left: 36px;
  }
  .date-bar .time {
    flex: 1;
    font-family: "Bebas Neue", sans-serif;
    font-size: 60px;
    line-height: 78px;
    color: var(--white);
    text-align: center;
  }
  .venue {
    position: absolute;
    top: 884px; left: 133px; width: 666px;
    display: flex; align-items: center; gap: 18px;
    font-family: "Yeseva One", serif;
    font-size: 40px;
    color: var(--red);
    white-space: nowrap;
  }
  .venue::before, .venue::after {
    content: ""; flex: 1; height: 2px; background: var(--red);
  }
  .address {
    position: absolute;
    top: 948px; left: 0; right: 0;
    text-align: center;
    font-family: "Yeseva One", serif;
    font-size: 24px;
    letter-spacing: 1px;
    color: var(--ink-soft);
  }
  .tickets {
    position: absolute;
    top: 990px; left: 133px;
    width: 666px; height: 82px;
    border-radius: 41px;
    border: 3px solid var(--silver);
    background: linear-gradient(90deg, var(--gold-dark), var(--gold-light) 60%, var(--gold));
    display: flex; align-items: center;
    padding: 4px;
  }
  .tickets .label {
    width: 218px; height: 100%;
    border-radius: 36px;
    background: linear-gradient(90deg, #0e0e0e, #444);
    font-family: "Bebas Neue", sans-serif;
    font-size: 46px;
    color: var(--white);
    display: flex; align-items: center; justify-content: center;
  }
  .tickets .url {
    flex: 1;
    text-align: center;
    font-family: "Bebas Neue", sans-serif;
    font-size: 48px;
    color: var(--ink);
  }
  .pricing {
    position: absolute;
    top: 1086px; left: 0; right: 0;
    text-align: center;
    font-family: "Bebas Neue", sans-serif;
    font-size: 38px;
    color: var(--ink-soft);
  }
</style>
</head>
<body>
  <main class="poster">
    <div class="poster-inner">
      <h1 class="title-script">HarmoNest Ensemble</h1>
      <div class="rule rule-top"></div>
      <h2 class="title-caps">Jubilee</h2>
      <div class="rule rule-bottom"></div>

      <svg class="photo" viewBox="0 0 930 560" role="img" aria-label="Group photo of the four ensemble members in black outfits holding gold saxophones">
        <defs>
          <linearGradient id="photoTone" x1="0" y1="0" x2="1" y2="1">
            <stop offset="0" stop-color="#e2e2e7"/>
            <stop offset="0.5" stop-color="#cfcfd6"/>
            <stop offset="1" stop-color="#c2c2ca"/>
          </linearGradient>
        </defs>
        <path fill="url(#photoTone)" d="M0 105 L40 95 L70 80 L110 70 L150 60 L190 48 L230 40 L280 34 L330 26 L380 20 L430 28 L470 18 L520 14 L570 24 L620 12 L680 8 L740 4 L800 2 L860 0 L930 8 L930 440 L900 452 L860 448 L820 462 L780 455 L740 470 L700 476 L660 470 L620 488 L580 492 L540 500 L500 512 L460 518 L420 524 L380 520 L340 526 L300 536 L260 538 L220 546 L180 552 L140 550 L100 556 L60 554 L20 560 L0 558 Z"/>
      </svg>

      <div class="date-bar">
        <div class="date">Sunday Oct 2, 2022</div>
        <div class="time">2-4 P.M.</div>
      </div>

      <p class="venue">Brindle9 Alehouse</p>
      <p class="address">413 Marlowe Ct #200, Sacramento, CA 95821</p>

      <div class="tickets">
        <span class="label">Tickets:</span>
        <span class="url">WWW.TIXOLVO.COM</span>
      </div>

      <p class="pricing">General seating: $15 for adults and $10 for students</p>
    </div>
  </main>
</body>
</html>
```